3 Banners for Large Scale Print for Conference

We need 3 -32"x80" banners designed for a conference. The design needs to make it look as if the 3 separate units are one big unit. We will use this for a conference. We are a software firm that specializes in delivering online software to support customer surveys, assessments, and portals. From large corporations, to nonprofits, our software solutions are used to support their customer and stakeholder needs. I am attaching an example of how the 3 units could look so it flows like a single unit. I also attached an eps of our logo. It's in our colors of burgundy and silver.

Our corporate website is www.tervalinkworks.com . The design needs no bleed. I am looking for a professional awesome design.

I attached the eps of the logo which has the corporate colors and font. Take a look at the banner image I uploaded. I like how it done. Our words could be Survey, Assessment, Customer Engagement, Solutions, Secure Portals, Data Analysis, but we are open to creative ideas. Because the bottoms of the banners might be obscured but the table, I think an image might need to be there, but again I am open to your vision as long as it gives up a high-end upscale design.

Target Market(s)

Business Owners, Corporations, Nonprofits,

Industry/Entity Type

Software

Font styles to use
Sans Serif

Requirements
Must have
• The 3 banners must look like the form a larger image just with a gap because of them being 3 separate images. See the picture that I uploaded.
Should not have
• odd colors, amateur efforts. grainy images,

```html
<!DOCTYPE html>
<html lang="en">
<head>
<meta charset="utf-8">
<title>Tervalink Works – Conference Banners</title>
<link rel="stylesheet" href="https://fonts.googleapis.com/css2?family=Questrial&display=swap">
<style>
  :root {
    --burgundy: #7b1a2c;
    --burgundy-deep: #5e1220;
    --charcoal: #3c3b3d;
    --silver: #8d8888;
    --silver-band: #b7b2b2;
    --paper: #ffffff;
    --gap: #ffffff;
  }
  html, body {
    margin: 0;
    padding: 0;
    width: 1200px;
    height: 1000px;
    overflow: hidden;
    background: var(--paper);
  }
  .banner-set {
    position: relative;
    width: 1200px;
    height: 1000px;
    font-family: "Questrial", "Helvetica Neue", Arial, sans-serif;
  }
  .chevron-band {
    position: absolute;
    left: 0;
    top: 0;
    width: 1200px;
    height: 420px;
  }
  .gutter {
    position: absolute;
    top: 0;
    width: 10px;
    height: 1000px;
    background: var(--gap);
  }
  .gutter--one { left: 396px; }
  .gutter--two { left: 796px; }
  .panel {
    position: absolute;
    top: 0;
    height: 1000px;
  }
  .panel--survey { left: 0; width: 396px; }
  .panel--engagement { left: 406px; width: 390px; }
  .panel--portals { left: 806px; width: 394px; }

  .brand {
    position: absolute;
    top: 10px;
    width: 300px;
    display: flex;
    flex-direction: column;
    align-items: center;
  }
  .panel--survey .brand { left: 33px; }
  .panel--engagement .brand { left: 29px; }
  .panel--portals .brand { left: 34px; }
  .brand__mark {
    width: 104px;
    height: 104px;
    border-radius: 50%;
    background: var(--burgundy);
  }
  .brand__name {
    margin-top: 30px;
    font-size: 24px;
    line-height: 1;
    letter-spacing: 2.4px;
    color: var(--charcoal);
    text-transform: uppercase;
    white-space: nowrap;
  }

  .headline {
    position: absolute;
    top: 384px;
    margin: 0;
    font-weight: 400;
    text-transform: uppercase;
    line-height: 1;
    white-space: nowrap;
  }
  .headline__lead {
    display: block;
    font-size: 28px;
    letter-spacing: -1.2px;
    color: var(--silver);
  }
  .headline__key {
    display: block;
    margin-top: -1px;
    font-size: 30px;
    letter-spacing: 2.6px;
    color: var(--burgundy);
  }
  .panel--survey .headline { left: 82px; }
  .panel--engagement .headline { left: 12px; }
  .panel--portals .headline { left: 45px; }

  .photo {
    position: absolute;
    left: 0;
    width: 100%;
  }
  .photo--agent {
    top: 505px;
    height: 410px;
    background: radial-gradient(ellipse 55% 60% at 50% 48%, #e8c2a8 0%, #e9cdb8 35%, #c9d7e8 70%, #ffffff 100%);
  }
  .photo--handshake {
    top: 458px;
    height: 457px;
    background: linear-gradient(165deg, #ecebe8 0%, #d9d2ca 30%, #3a3a42 60%, #2a2a30 80%, #ece9e6 100%);
  }
  .photo--laptop {
    top: 458px;
    height: 457px;
    background: linear-gradient(95deg, #e4e8e9 0%, #cfd5d7 40%, #6b6d72 68%, #4a4c51 85%, #e6e6e6 100%);
  }

  .footer-band {
    position: absolute;
    left: 0;
    bottom: 0;
    width: 100%;
    height: 80px;
    background: var(--silver-band);
    display: flex;
    align-items: center;
    justify-content: center;
  }
  .footer-band__url {
    font-size: 18px;
    letter-spacing: 1.8px;
    color: var(--burgundy);
    padding-top: 6px;
  }
</style>
</head>
<body>
<main class="banner-set">

  <svg class="chevron-band" viewBox="0 0 1200 420" aria-hidden="true">
    <defs>
      <linearGradient id="band-fade" x1="0" y1="0" x2="1200" y2="0" gradientUnits="userSpaceOnUse">
        <stop offset="0" stop-color="#7b1a2c" stop-opacity="0.75"/>
        <stop offset="0.3" stop-color="#6a1626" stop-opacity="0.95"/>
        <stop offset="0.55" stop-color="#7b1a2c" stop-opacity="0.9"/>
        <stop offset="0.72" stop-color="#8a2a3a" stop-opacity="0.7"/>
        <stop offset="0.85" stop-color="#c9c4c4" stop-opacity="0.55"/>
        <stop offset="1" stop-color="#e3e0e0" stop-opacity="0.35"/>
      </linearGradient>
      <linearGradient id="band-shadow" x1="0" y1="0" x2="400" y2="0" gradientUnits="userSpaceOnUse">
        <stop offset="0" stop-color="#3c3b3d" stop-opacity="0.15"/>
        <stop offset="1" stop-color="#3c3b3d" stop-opacity="0.8"/>
      </linearGradient>
    </defs>
    <polygon fill="url(#band-shadow)" points="120,275 290,320 396,300 396,318 290,364 120,320"/>
    <polygon fill="url(#band-fade)" points="0,220 290,298 592,180 1200,300 1200,390 592,250 290,362 0,292"/>
  </svg>

  <section class="panel panel--survey">
    <div class="brand"><span class="brand__mark"></span><span class="brand__name">Tervalink Works</span></div>
    <h2 class="headline"><span class="headline__lead">Data Analyses</span><span class="headline__key">Survey</span></h2>
    <div class="photo photo--agent" role="img" aria-label="Smiling support agent wearing a headset, cut out on white"></div>
    <footer class="footer-band"><span class="footer-band__url">www.tervalinkworks.com</span></footer>
  </section>

  <section class="panel panel--engagement">
    <div class="brand"><span class="brand__mark"></span><span class="brand__name">Tervalink Works</span></div>
    <h2 class="headline"><span class="headline__lead">Customer Engagement.</span><span class="headline__key">Solutions</span></h2>
    <div class="photo photo--handshake" role="img" aria-label="Business team in suits shaking hands across a meeting table"></div>
    <footer class="footer-band"><span class="footer-band__url">www.tervalinkworks.com</span></footer>
  </section>

  <section class="panel panel--portals">
    <div class="brand"><span class="brand__mark"></span><span class="brand__name">Tervalink Works</span></div>
    <h2 class="headline"><span class="headline__lead">Secure Portals</span><span class="headline__key">Assessment</span></h2>
    <div class="photo photo--laptop" role="img" aria-label="Businessman in a grey suit working on a laptop in a bright office"></div>
    <footer class="footer-band"><span class="footer-band__url">www.tervalinkworks.com</span></footer>
  </section>

  <div class="gutter gutter--one"></div>
  <div class="gutter gutter--two"></div>
</main>
</body>
</html>
```